New web page, 2 companies on the one page

A new web page for an engineering consultancy and maintenance management company

Carlow & Associates is the parent company covering the design and consultancy
Viltrop Engineering is the Maintenance and Reliability company

Target Market(s)

Food & Beverage, ingredients Manufacturing
engineering managers

Coding

Coded - Design and coding required

Number of Pages Required

1 page

Font styles to use
Other font styles liked:
• Roboto

Colors
1861ab
85acd3
d0dfed
cee9f5

```html
<!DOCTYPE html>
<html lang="en">
<head>
<meta charset="utf-8">
<title>Viltrop Engineering – Maintenance &amp; Reliability</title>
<link rel="stylesheet" href="https://fonts.googleapis.com/css2?family=Roboto:wght@400;500;700&family=Montserrat:wght@400;500;600;700&family=Jost:wght@300;400;500;600&display=swap">
<style>
:root{
  --navy:#0f1233;
  --navy-deep:#0a0c26;
  --blue:#1861ab;
  --blue-mid:#85acd3;
  --blue-pale:#d0dfed;
  --sky-pale:#cee9f5;
  --ink:#1c2233;
  --muted:#5d6474;
  --white:#ffffff;
  --grey:#7b7f88;
}
*{margin:0;padding:0;box-sizing:border-box}
html,body{width:1200px;height:3958px;overflow:hidden;background:var(--white)}
body{font-family:"Montserrat",sans-serif;color:var(--ink)}
.page{position:relative;width:1200px;height:3958px;overflow:hidden}
.abs{position:absolute}

/* hero */
.hero{position:absolute;left:0;top:0;width:1200px;height:720px}
.hero-bg{position:absolute;inset:0}
.brand{position:absolute;display:flex;align-items:center;gap:12px;color:var(--white);font-family:"Montserrat",sans-serif;font-weight:700;letter-spacing:1px}
.brand-dot{width:44px;height:44px;border-radius:50%;background:var(--blue)}
.hero .brand{left:122px;top:52px;font-size:34px}
.topbar{position:absolute;top:18px;left:855px;display:flex;align-items:center;gap:70px;color:var(--white);font-family:"Roboto",sans-serif;font-size:14px}
.topbar span{display:flex;align-items:center;gap:8px}
.nav-line{position:absolute;left:470px;top:56px;width:730px;height:1px;background:rgba(255,255,255,.25)}
.nav-line.bottom{top:108px}
.nav{position:absolute;top:72px;left:540px;display:flex;font-family:"Roboto",sans-serif;font-weight:500;font-size:16px;color:var(--white)}
.nav a{color:inherit;text-decoration:none;padding:0 34px;border-left:1px solid rgba(255,255,255,.3)}
.nav a:first-child{border-left:none}
.hero-photo{position:absolute;left:610px;top:160px;width:460px;height:460px;border-radius:50%;background:radial-gradient(circle at 50% 45%,#6d8fc4 0%,#2f4a8a 30%,#141a46 65%,rgba(15,18,51,0) 72%)}
.hero-title{position:absolute;left:180px;top:218px;font-family:"Roboto",sans-serif;font-weight:700;font-size:52px;line-height:58px;color:var(--white);letter-spacing:-.5px}
.btn-pill{position:absolute;border-radius:30px;display:flex;align-items:center;justify-content:center;text-decoration:none}
.hero-btn{left:181px;top:432px;width:171px;height:47px;background:var(--blue);color:var(--white);font-family:"Roboto",sans-serif;font-weight:700;font-size:16px}
.arrow-btn{position:absolute;width:44px;height:44px;border-radius:50%;display:flex;align-items:center;justify-content:center}
.arrow-btn.prev{left:84px;top:306px;background:#4b4e63}
.arrow-btn.next{left:1067px;top:306px;background:var(--white)}
.dots{position:absolute;left:519px;top:636px;display:flex;gap:10px}
.dots i{display:block;width:48px;height:4px;background:var(--white)}
.dots i.on{background:var(--blue)}

/* about */
.about-photo{position:absolute;left:120px;top:784px;width:418px;height:418px;border-radius:50%;background:linear-gradient(135deg,#c9d4e2,#5a6a86 55%,#1b2a4d)}
.about-ring{position:absolute;left:130px;top:780px;width:418px;height:418px;border-radius:50%;border:2px dotted var(--blue)}
.sec-title{font-family:"Montserrat",sans-serif;font-weight:400;font-size:37px;color:var(--grey);letter-spacing:-.5px}
.sec-title b{color:var(--blue);font-weight:700}
.about-title{position:absolute;left:628px;top:826px}
.about-text{position:absolute;left:628px;top:898px;width:440px;font-size:13px;line-height:23px;color:var(--muted)}
.about-text .lead{font-size:15.5px;line-height:26px;color:var(--ink);font-weight:500;margin-bottom:14px}
.about-text p{margin-bottom:17px}

/* services */
.svc-stem{position:absolute;left:599px;top:1266px;width:2px;height:46px;background:#6b6f78}
.svc-stem::after{content:"";position:absolute;left:-3px;bottom:-4px;width:8px;height:8px;border-radius:50%;background:#6b6f78}
.svc-title{position:absolute;left:0;width:1200px;top:1328px;text-align:center}
.svc-sub{position:absolute;left:380px;width:440px;top:1385px;text-align:center;font-size:13px;line-height:23px;color:var(--muted)}
.svc-grid{position:absolute;left:135px;top:1483px;width:936px;display:grid;grid-template-columns:repeat(3,312px);grid-template-rows:330px 323px}
.svc-card{position:relative;padding:48px 40px 0 40px;border-right:1px solid #eef0f4;border-bottom:1px solid #eef0f4}
.svc-card:nth-child(3n){border-right:none}
.svc-card:nth-child(n+4){border-bottom:none}
.svc-card.active{background:var(--white);box-shadow:0 6px 30px rgba(24,40,80,.12)}
.svc-icon{width:60px;height:60px;margin-bottom:18px}
.svc-card h3{font-family:"Montserrat",sans-serif;font-weight:500;font-size:17px;line-height:23px;color:var(--ink);margin-bottom:18px}
.svc-card p{font-size:12px;line-height:20px;color:var(--muted);margin-bottom:18px}
.learn{font-size:12px;font-weight:600;color:var(--blue);text-decoration:none;display:flex;align-items:center;gap:8px}

/* cta */
.cta{position:absolute;left:0;top:2220px;width:1200px;height:530px}
.cta-ring{position:absolute;border-radius:50%}
.cta-kicker{position:absolute;left:516px;top:2366px;font-family:"Jost",sans-serif;font-weight:300;font-size:34px;color:var(--blue-pale)}
.cta-head{position:absolute;left:516px;top:2418px;width:390px;font-family:"Jost",sans-serif;font-weight:600;font-size:40px;line-height:54px;letter-spacing:-.6px;color:var(--white);white-space:nowrap}
.cta-btn{left:518px;top:2567px;width:198px;height:50px;background:var(--white);color:var(--blue);font-family:"Jost",sans-serif;font-size:20px}
.cta-person{position:absolute;left:925px;top:2176px;width:120px;height:550px;border-radius:60px 60px 36px 36px;background:linear-gradient(180deg,#c9a48c 0%,#d23a3a 18%,#c83434 40%,#1d2a4e 55%,#16203d 100%)}

/* blog */
.blog-card{position:absolute;top:2842px;width:288px;height:382px;background:var(--white);box-shadow:0 4px 22px rgba(20,30,60,.12)}
.blog-img{height:174px}
.blog-body{padding:20px 22px}
.blog-meta{font-family:"Jost",sans-serif;font-size:12px;color:var(--grey);margin-bottom:6px}
.blog-body h4{font-family:"Jost",sans-serif;font-weight:400;font-size:17px;line-height:21px;color:var(--ink);margin-bottom:8px}
.blog-body p{font-family:"Jost",sans-serif;font-size:13px;line-height:19px;color:var(--muted);margin-bottom:10px}
.blog-body a{font-family:"Jost",sans-serif;font-size:14px;color:var(--blue)}

/* footer */
.footer-bg{position:absolute;left:0;top:3260px;width:1200px;height:698px}
.footer .brand{left:140px;top:3448px;font-size:34px}
.contact-list{position:absolute;left:135px;top:3570px;font-family:"Jost",sans-serif;font-size:15px;line-height:21px;color:var(--white)}
.contact-row{display:flex;gap:26px;align-items:center;margin-bottom:26px}
.c-icon{width:36px;height:36px;border-radius:50%;background:#2a2e4a;display:flex;align-items:center;justify-content:center;flex:none}
.socials{position:absolute;left:135px;top:3778px;display:flex;gap:8px}
.socials i{display:block;width:35px;height:35px;border-radius:50%;background:var(--blue)}
.f-head{position:absolute;font-family:"Jost",sans-serif;font-size:19px;color:var(--white)}
.f-links{position:absolute;left:480px;top:3496px;list-style:none;font-family:"Jost",sans-serif;font-size:14px;color:var(--white)}
.f-links li{margin-bottom:12px}
.f-links li::before{content:"›";margin-right:10px}
.map-btn{position:absolute;left:480px;top:3700px;width:148px;height:66px;background:var(--blue);color:var(--white);font-family:"Jost",sans-serif;font-size:15px;display:flex;align-items:center;justify-content:center;gap:20px}
.field{position:absolute;left:737px;width:333px;height:38px;border:1px solid #2c3050;background:#10132e;color:#a9acbb;font-family:"Jost",sans-serif;font-size:14px;padding:9px 20px}
.send{position:absolute;left:737px;top:3784px;width:134px;height:38px;background:var(--blue);color:var(--white);font-family:"Jost",sans-serif;font-size:15px;display:flex;align-items:center;justify-content:center}
.f-rule{position:absolute;left:132px;top:3875px;width:936px;height:1px;background:#2a2e4a}
.copy{position:absolute;left:0;width:1200px;top:3903px;text-align:center;font-family:"Jost",sans-serif;font-size:15px;color:#b7b9c6}
</style>
</head>
<body>
<div class="page">

  <section class="hero">
    <svg class="hero-bg" width="1200" height="720" viewBox="0 0 1200 720" aria-hidden="true">
      <rect width="1200" height="720" fill="#0f1233"/>
      <path d="M0 618 L600 706 L1200 618 L1200 720 L0 720Z" fill="#ffffff"/>
      <path d="M0 616 L598 700 L598 712 L0 628Z" fill="#6e7078"/>
      <path d="M602 700 L1200 612 L1200 624 L602 712Z" fill="#1861ab"/>
    </svg>
    <div class="hero-photo" role="img" aria-label="Open hands holding glowing gears inside a network of connected points"></div>
    <div class="brand"><span class="brand-dot"></span>VILTROP</div>
    <div class="topbar">
      <span><svg width="16" height="16" viewBox="0 0 24 24" fill="none" stroke="#fff" stroke-width="2"><path d="M5 3h4l2 5-3 2a12 12 0 0 0 6 6l2-3 5 2v4a2 2 0 0 1-2 2A18 18 0 0 1 3 5a2 2 0 0 1 2-2z"/></svg>(680) 555-0192</span>
      <span><svg width="22" height="16" viewBox="0 0 22 16" fill="none" stroke="#fff" stroke-width="1.6"><rect x="1" y="1" width="20" height="14"/><path d="M1 1l10 8 10-8M1 15l7-6M21 15l-7-6"/></svg></span>
    </div>
    <div class="nav-line"></div><div class="nav-line bottom"></div>
    <nav class="nav"><a href="#">HOME</a><a href="#">ABOUT US</a><a href="#">SERVICES ▾</a><a href="#">CONTACT US</a></nav>
    <h1 class="hero-title">Engineering<br>Maintenance &amp;<br>Reliability company</h1>
    <a class="btn-pill hero-btn" href="#">WHO WE ARE</a>
    <span class="arrow-btn prev"><svg width="12" height="12" viewBox="0 0 12 12" fill="none" stroke="#fff" stroke-width="2"><path d="M8 1L3 6l5 5"/></svg></span>
    <span class="arrow-btn next"><svg width="12" height="12" viewBox="0 0 12 12" fill="none" stroke="#1861ab" stroke-width="2"><path d="M4 1l5 5-5 5"/></svg></span>
    <div class="dots"><i></i><i class="on"></i><i></i></div>
  </section>

  <svg class="abs" style="left:0;top:690px" width="360" height="470" viewBox="0 0 360 470" aria-hidden="true">
    <path d="M250 0 C330 80 360 240 260 360 C180 450 60 470 0 455" fill="none" stroke="#c8ccd3" stroke-dasharray="3 4"/>
  </svg>
  <div class="about-photo" role="img" aria-label="Two business colleagues reviewing work on a tablet"></div>
  <div class="about-ring"></div>
  <h2 class="sec-title about-title">ABOUT <b>VILTROP</b></h2>
  <div class="about-text">
    <p class="lead">Carlow &amp; Associates is specialised manufacturing engineering support organisation that can provide fast, nimble, and flexible services.</p>
    <p>We have a proven track record in delivering tangible outcomes in process design and fit-out, project management, manufacturing process and maintenance design and execution.</p>
    <p>Our specialist focus in food manufacturing across a range of sectors allows our team to deliver real benefits to performance and recognition of the clients investment.</p>
  </div>

  <div class="svc-stem"></div>
  <h2 class="sec-title svc-title">OUR <b>SERVICES</b></h2>
  <p class="svc-sub">Our specialist focus in food manufacturing across a range of sectors allows our team to deliver real benefits to performance.</p>

  <div class="svc-grid">
    <div class="svc-card">
      <svg class="svc-icon" viewBox="0 0 60 60" fill="none" stroke="#1c2a55" stroke-width="2"><rect x="2" y="14" width="30" height="36" fill="#eef1f5" stroke="none"/><circle cx="16" cy="12" r="4"/><circle cx="44" cy="30" r="4"/><circle cx="16" cy="48" r="4"/><path d="M20 12h18a6 6 0 0 1 0 12M40 30H22a6 6 0 0 0 0 12h-2"/></svg>
      <h3>Process &amp;<br>Facilities Design</h3>
      <p>Lorem Ipsum is simply dummy text of the printing and typesetting industry. Lorem Ipsum has been.</p>
      <a class="learn" href="#">Learn More →</a>
    </div>
    <div class="svc-card active">
      <svg class="svc-icon" viewBox="0 0 60 60" fill="none" stroke="#1c2a55" stroke-width="2"><rect x="2" y="14" width="30" height="36" fill="#eef1f5" stroke="none"/><circle cx="26" cy="22" r="10"/><circle cx="26" cy="22" r="4"/><circle cx="46" cy="44" r="7"/><path d="M32 30l9 8"/></svg>
      <h3>Project<br>Management</h3>
      <p>Lorem Ipsum is simply dummy text of the printing and typesetting industry. Lorem Ipsum has been.</p>
      <a class="learn" href="#">Learn More →</a>
    </div>
    <div class="svc-card">
      <svg class="svc-icon" viewBox="0 0 60 60" fill="none" stroke="#1c2a55" stroke-width="2"><rect x="2" y="14" width="30" height="36" fill="#eef1f5" stroke="none"/><rect x="14" y="10" width="42" height="30" rx="2"/><path d="M28 48h14M35 40v8"/><circle cx="28" cy="25" r="5"/><circle cx="43" cy="25" r="5"/></svg>
      <h3>Major Equipment &amp;<br>Services Installation</h3>
      <p>Lorem Ipsum is simply dummy text of the printing and typesetting industry. Lorem Ipsum has been.</p>
      <a class="learn" href="#">Learn More →</a>
    </div>
    <div class="svc-card">
      <svg class="svc-icon" viewBox="0 0 60 60" fill="none" stroke="#1c2a55" stroke-width="2"><rect x="2" y="14" width="30" height="36" fill="#eef1f5" stroke="none"/><circle cx="22" cy="22" r="10"/><circle cx="22" cy="22" r="4"/><circle cx="40" cy="40" r="10"/><circle cx="40" cy="40" r="4"/></svg>
      <h3>Engineering and<br>Maintenance</h3>
      <p>Lorem Ipsum is simply dummy text of the printing and typesetting industry. Lorem Ipsum has been.</p>
      <a class="learn" href="#">Learn More →</a>
    </div>
    <div class="svc-card">
      <svg class="svc-icon" viewBox="0 0 60 60" fill="none" stroke="#1c2a55" stroke-width="2"><rect x="2" y="14" width="30" height="36" fill="#eef1f5" stroke="none"/><circle cx="34" cy="20" r="12"/><circle cx="34" cy="20" r="5"/><rect x="22" y="34" width="18" height="20" rx="2"/><path d="M26 40h10M26 46h10"/></svg>
      <h3>Maintenance<br>Execution</h3>
      <p>Lorem Ipsum is simply dummy text of the printing and typesetting industry. Lorem Ipsum has been.</p>
      <a class="learn" href="#">Learn More →</a>
    </div>
    <div class="svc-card">
      <svg class="svc-icon" viewBox="0 0 60 60" fill="none" stroke="#1c2a55" stroke-width="2"><rect x="2" y="14" width="30" height="36" fill="#eef1f5" stroke="none"/><rect x="18" y="8" width="28" height="40" rx="2"/><path d="M26 6h12v6H26zM24 20h16M24 27h10"/><circle cx="40" cy="40" r="8"/><path d="M46 46l8 8"/></svg>
      <h3>Vision Inspection<br>Systems</h3>
      <p>Lorem Ipsum is simply dummy text of the printing and typesetting industry. Lorem Ipsum has been.</p>
      <a class="learn" href="#">Learn More →</a>
    </div>
  </div>

  <section class="cta">
    <svg width="1200" height="530" viewBox="0 0 1200 530" aria-hidden="true">
      <path d="M0 80 L600 10 L1200 80 L1200 530 L0 530Z" fill="#1861ab"/>
    </svg>
  </section>
  <div class="cta-ring" style="left:125px;top:2338px;width:322px;height:322px;border:1px solid rgba(208,223,237,.35)"></div>
  <div class="cta-ring" style="left:150px;top:2362px;width:274px;height:274px;border:1px solid rgba(208,223,237,.45)"></div>
  <div class="cta-ring" style="left:169px;top:2382px;width:236px;height:236px;background:#124f90"></div>
  <div class="cta-person" role="img" aria-label="Smiling woman in a red top holding a phone"></div>
  <p class="cta-kicker">Change starts here</p>
  <h2 class="cta-head">Take your first step<br>towards RESULT.</h2>
  <a class="btn-pill cta-btn" href="#">Email us Today</a>

  <article class="blog-card" style="left:132px">
    <div class="blog-img" role="img" aria-label="Hands reviewing printed charts on a desk" style="background:linear-gradient(135deg,#7f8fa5,#d8d2c4 60%,#4a5a72)"></div>
    <div class="blog-body"><div class="blog-meta">By Admin</div><h4>Lorem Ipsum is simply dummy text of the printing</h4><p>There are many variations of passages of available but majority have alteration</p><a href="#">Read More</a></div>
  </article>
  <article class="blog-card" style="left:456px">
    <div class="blog-img" role="img" aria-label="Hand touching a digital gear interface" style="background:linear-gradient(135deg,#1f3f6e,#7fa6cf 55%,#2a4a7c)"></div>
    <div class="blog-body"><div class="blog-meta">By Admin</div><h4>Lorem Ipsum is simply dummy text of the printing</h4><p>There are many variations of passages of available but majority have alteration</p><a href="#">Read More</a></div>
  </article>
  <article class="blog-card" style="left:780px">
    <div class="blog-img" role="img" aria-label="Team of colleagues discussing documents" style="background:linear-gradient(135deg,#8a7868,#e6e0d8 55%,#9aa0a8)"></div>
    <div class="blog-body"><div class="blog-meta">By Admin</div><h4>Lorem Ipsum is simply dummy text of the printing</h4><p>There are many variations of passages of available but majority have alteration</p><a href="#">Read More</a></div>
  </article>

  <footer class="footer">
    <svg class="footer-bg" width="1200" height="698" viewBox="0 0 1200 698" aria-hidden="true">
      <path d="M0 20 C200 90 420 110 640 90 C860 70 1050 40 1200 0 L1200 698 L0 698Z" fill="#c9cbd3"/>
      <path d="M0 50 C200 120 420 140 640 118 C860 98 1050 70 1200 40 L1200 698 L0 698Z" fill="#0f1233"/>
    </svg>
    <div class="brand"><span class="brand-dot"></span>VILTROP</div>
    <div class="contact-list">
      <div class="contact-row"><span class="c-icon"><svg width="14" height="16" viewBox="0 0 14 18" fill="#fff"><path d="M7 0a7 7 0 0 1 7 7c0 5-7 11-7 11S0 12 0 7a7 7 0 0 1 7-7zm0 4a3 3 0 1 0 0 6 3 3 0 0 0 0-6z"/></svg></span><span>Halden Court, Brookfield,<br>NY 10018, USA</span></div>
      <div class="contact-row"><span class="c-icon"><svg width="10" height="16" viewBox="0 0 10 16" fill="none" stroke="#fff" stroke-width="1.6"><rect x="1" y="1" width="8" height="14" rx="1.5"/></svg></span><span>+1 23 555 0147<br>Support 24/7 Weekdays</span></div>
      <div class="contact-row"><span class="c-icon"><svg width="16" height="12" viewBox="0 0 16 12" fill="none" stroke="#fff" stroke-width="1.4"><rect x="1" y="1" width="14" height="10"/><path d="M1 1l7 6 7-6"/></svg></span><span>info@viltrop-eng.com</span></div>
    </div>
    <div class="socials"><i></i><i></i><i></i><i></i></div>

    <h5 class="f-head" style="left:480px;top:3453px">Info</h5>
    <ul class="f-links"><li>Home</li><li>About Us</li><li>Services</li><li>Blog</li><li>Contact Us</li></ul>
    <div class="map-btn">Our Map <svg width="34" height="34" viewBox="0 0 34 34" fill="none" stroke="#fff" stroke-width="1.4"><path d="M17 3a8 8 0 0 1 8 8c0 6-8 13-8 13S9 17 9 11a8 8 0 0 1 8-8z"/><circle cx="17" cy="11" r="3"/><path d="M4 31l5-9h4M30 31l-5-9h-4M4 31h26"/></svg></div>

    <h5 class="f-head" style="left:736px;top:3453px">Get In Touch</h5>
    <div class="field" style="top:3508px">Your Name</div>
    <div class="field" style="top:3564px">Your Email Address</div>
    <div class="field" style="top:3620px">Mobile</div>
    <div class="field" style="top:3676px;height:92px">Comments</div>
    <div class="send">Send To Us</div>

    <div class="f-rule"></div>
    <p class="copy">© 2021 Viltrop Engineering Reliability. All Rights Reserved.</p>
  </footer>
</div>
</body>
</html>
```